Website Design AI Digital Marketing Tool for Small Businesses

We are a marketing saas that is selling an app that allows business owners to launch digital marketing campaigns in one click. Our value proposition is to help them grow their business in one click with pre-vetted marketers armed with AI.

We want a modern website design that looks like a professional tech startup / saas. Use the same content on brevora.io and make it look incredible. We want it to stand out and use big bold colors and text so that it's energetic and creative but still modern.

Pages are:
Home - brevora.io
Pricing - brevora.io/pricing
Features - https://brevora.io/features/
Marketing - https://brevora.io/marketing/

EXAMPLES
https://quandle.sitebuildr.io/
https://harbor-venture-sitebuildr-layout.sitebuildr.io/home-02

We really want a professional tech company feel. It needs to look like the best company with the best team in the world created it.

Target Market(s)

We are targeting small businesses to help them with their digital marketing

Industry/Entity Type

Tech

Coding

Coded - Design and coding required

Number of Pages Required

4 page

Font styles to use
Sans Serif
Other font styles liked:
• Work Sans

Colors
0094D4
00A9DD
6FCCEA
C7EBF8
E9F6FB

Requirements
Must have
• Modern, bright colors, same / similar content as existing site
Nice to have
• Big bold text and brand colors like plumtrex - but also techy and modern
Should not have
• nothing that doesnt fit the brand

```html
<!DOCTYPE html>
<html lang="en">
<head>
<meta charset="utf-8">
<title>Brevora — The App to Automate Your Small Business Growth</title>
<link rel="stylesheet" href="https://fonts.googleapis.com/css2?family=Montserrat:wght@500;600;700&family=Work+Sans:wght@400;500;600&display=swap">
<style>
:root{
  --blue:#0094D4;
  --blue-bright:#00A9DD;
  --sky:#6FCCEA;
  --ice:#C7EBF8;
  --mist:#E9F6FB;
  --ink:#1c1c1c;
  --soft-bg:#f4f5f7;
  --night:#000000;
  --pill:#2e2e2e;
  --line:#d9dce0;
}
*{box-sizing:border-box;margin:0;padding:0}
html,body{width:1200px;height:4221px;overflow:hidden;background:#fff}
body{position:relative;font-family:"Work Sans",Arial,sans-serif;color:var(--ink)}
.section{position:absolute;left:0;width:1200px}
.abs{position:absolute}
.heading{font-family:"Montserrat",Arial,sans-serif;font-weight:500;font-size:33px;line-height:49px;letter-spacing:.5px;text-transform:uppercase;color:var(--ink)}
.heading .accent{color:var(--blue)}
.body-copy{font-size:15px;font-weight:500;line-height:34px;color:var(--ink)}
.center{left:0;right:0;text-align:center}
.btn{position:absolute;display:flex;align-items:center;justify-content:center;border-radius:26px;font-family:"Montserrat",Arial,sans-serif;font-weight:600;font-size:17px;text-transform:uppercase;letter-spacing:.3px}
.btn-solid{background:var(--blue);color:#fff}
.btn-ghost{border:2px solid var(--blue);color:var(--blue);background:#fff}

/* header */
.brand{position:absolute;display:flex;align-items:center;gap:10px;font-family:"Work Sans",sans-serif;font-weight:400;font-size:40px;color:#3a3a3a;letter-spacing:.5px}
.brand-mark{width:30px;height:30px;background:var(--blue-bright)}
.nav-pill{position:absolute;left:421px;top:38px;width:428px;height:46px;border-radius:23px;background:var(--pill)}
.nav-home{position:absolute;left:28px;top:9px;width:36px;height:28px;border-radius:14px;background:#fff;display:flex;align-items:center;justify-content:center}
.nav-item{position:absolute;top:0;line-height:46px;font-family:"Montserrat",sans-serif;font-weight:700;font-size:12px;color:#fff;letter-spacing:.3px}
.header-cta{position:absolute;left:949px;top:50px;font-family:"Montserrat",sans-serif;font-weight:600;font-size:15px;color:var(--blue);text-decoration:underline;letter-spacing:.3px}

.hero-kicker{top:166px;font-family:"Montserrat",sans-serif;font-weight:500;font-size:36px;letter-spacing:.8px;color:#222}
.hero-title{top:226px;font-family:"Montserrat",sans-serif;font-weight:600;font-size:58px;letter-spacing:1.5px;color:var(--blue)}

/* hero media */
.hero-media{position:absolute;left:0;top:20px;width:1200px;height:452px;background:linear-gradient(90deg,#c79b2e 0%,#d8c58a 18%,#e9e6df 38%,#dfe3ea 60%,#d9c6d6 75%,#b0524a 92%,#8c3a34 100%)}
.hero-rule{position:absolute;left:0;width:1200px;height:6px;background:var(--blue)}
.play{position:absolute;left:568px;top:216px;width:60px;height:60px;border-radius:50%;background:var(--blue);display:flex;align-items:center;justify-content:center}

/* accordion */
.acc-row{position:absolute;left:618px;width:470px;height:60px;display:flex;align-items:center}
.acc-row svg{flex:none}
.acc-label{margin-left:27px;font-family:"Montserrat",sans-serif;font-weight:600;font-size:19px;color:var(--blue);text-transform:uppercase;letter-spacing:.4px;flex:1}
.acc-plus{font-size:22px;color:#222;font-weight:400}
.acc-rule{position:absolute;left:618px;width:470px;height:1px;background:var(--line)}

/* cards */
.card-media{position:absolute;border-radius:4px}
.card-title{position:absolute;width:315px;text-align:center;font-family:"Montserrat",sans-serif;font-weight:600;font-size:17px;color:var(--blue);text-transform:uppercase;letter-spacing:.3px}
.card-text{position:absolute;width:335px;text-align:center;font-size:15px;font-weight:500;line-height:34px}

/* testimonials */
.avatar{position:absolute;border-radius:50%}
.arrow{position:absolute;width:32px;height:32px;border-radius:50%;display:flex;align-items:center;justify-content:center}

/* stats */
.stat{position:absolute;width:260px;text-align:center}
.stat-num{font-family:"Montserrat",sans-serif;font-weight:600;font-size:32px;color:var(--blue);margin-top:10px}
.stat-label{font-family:"Montserrat",sans-serif;font-weight:500;font-size:15px;color:#222;margin-top:6px;text-transform:uppercase}

/* partners */
.partner{position:absolute;top:167px;height:93px;background:#000;display:flex;align-items:center;justify-content:center;color:#fff;font-family:"Work Sans",sans-serif;font-weight:600;font-size:22px}
.dot{position:absolute;top:308px;width:26px;height:3px;background:var(--blue)}

/* footer */
.footer{background:var(--night);color:#fff}
.footer-links{position:absolute;top:286px;left:0;right:0;display:flex;justify-content:center;gap:26px;font-family:"Montserrat",sans-serif;font-weight:500;font-size:15px;text-transform:uppercase}
.contact-dot{position:absolute;width:44px;height:44px;border-radius:50%;background:var(--blue);display:flex;align-items:center;justify-content:center}
.contact-text{position:absolute;font-family:"Montserrat",sans-serif;font-weight:500;font-size:15px;text-transform:uppercase}
.social{position:absolute;width:32px;height:32px;border-radius:50%;border:2px solid #fff}
</style>
</head>
<body>

<header class="section" style="top:0;height:511px">
  <div class="brand" style="left:111px;top:30px"><span class="brand-mark"></span>brevora</div>
  <nav class="nav-pill">
    <span class="nav-home"><svg width="16" height="14" viewBox="0 0 16 14"><path d="M8 1 1 7h2v6h4V9h2v4h4V7h2z" fill="#2e2e2e"/></svg></span>
    <span class="nav-item" style="left:107px">PRICING ▾</span>
    <span class="nav-item" style="left:218px">FEATURES</span>
    <span class="nav-item" style="left:325px">CONTACT</span>
  </nav>
  <a class="header-cta">GET STARTED ⟶</a>

  <h1 class="abs center hero-kicker">THE APP TO AUTOMATE YOUR SMALL</h1>
  <div class="abs center hero-title">BUSINESS GROWTH</div>
  <p class="abs center body-copy" style="top:313px">The Only Marketing Platform for Small Businesses that Handles Your Marketing<br>in One Click.</p>
  <a class="btn btn-solid" style="left:425px;top:405px;width:170px;height:49px">Get Started</a>
  <a class="btn btn-ghost" style="left:605px;top:405px;width:169px;height:49px">How It Works</a>
</header>

<section class="section" style="top:511px;height:492px">
  <div class="hero-media" role="img" aria-label="Team collaborating over design-thinking sketches and app wireframes on a table"></div>
  <span class="hero-rule" style="top:20px"></span>
  <span class="hero-rule" style="top:466px"></span>
  <span class="play"><svg width="20" height="24" viewBox="0 0 20 24"><path d="M2 0 L20 12 L2 24 Z" fill="#fff"/></svg></span>
</section>

<section class="section" style="top:1003px;height:621px">
  <h2 class="abs heading" style="left:110px;top:74px;width:420px"><span class="accent">Online Marketing<br>Will</span> Never Be The<br>Same</h2>
  <p class="abs body-copy" style="left:110px;top:235px">Get a Fortune-500 Quality Web Presence and<br>a Personalized Action Plan</p>
  <a class="btn btn-solid" style="left:111px;top:331px;width:173px;height:51px">View Pricing</a>
  <a class="btn btn-ghost" style="left:292px;top:331px;width:169px;height:51px;font-size:16px">What's Included</a>

  <div class="acc-row" style="top:80px">
    <svg width="42" height="42" viewBox="0 0 42 42" fill="none" stroke="#333" stroke-width="1.6"><path d="M3 39 L18 12 L26 26 L30 20 L39 39 Z"/><path d="M18 12V3h9l-2 3 2 3h-9"/></svg>
    <span class="acc-label">Set Your Goals</span><span class="acc-plus">+</span>
  </div>
  <div class="acc-rule" style="top:149px"></div>
  <div class="acc-row" style="top:159px">
    <svg width="42" height="42" viewBox="0 0 42 42" fill="none" stroke="#333" stroke-width="1.6"><rect x="6" y="4" width="28" height="34" rx="2"/><path d="M11 12l2 2 4-4M20 12h10M11 21l2 2 4-4M20 21h10M11 30l2 2 4-4M20 30h10"/></svg>
    <span class="acc-label">Get Detailed Action Plan</span><span class="acc-plus">+</span>
  </div>
  <div class="acc-rule" style="top:225px"></div>
  <div class="acc-row" style="top:231px">
    <svg width="42" height="42" viewBox="0 0 42 42" fill="none" stroke="#333" stroke-width="1.6"><rect x="4" y="10" width="34" height="26" rx="2"/><path d="M4 12l17 12 17-12"/><path d="M16 18l10-6v14l-10-6z" stroke="#0094D4"/></svg>
    <span class="acc-label">Instant Marketing</span><span class="acc-plus">+</span>
  </div>
  <div class="acc-rule" style="top:299px"></div>
  <div class="acc-row" style="top:313px">
    <svg width="42" height="42" viewBox="0 0 42 42" fill="none" stroke="#333" stroke-width="1.6"><rect x="3" y="6" width="36" height="24" rx="2"/><path d="M15 36h12M21 30v6"/><rect x="8" y="11" width="11" height="9"/><path d="M23 12h11M23 16h11M23 20h7"/></svg>
    <span class="acc-label">AI+ Web Creation</span><span class="acc-plus">+</span>
  </div>
  <div class="acc-rule" style="top:384px"></div>
  <div class="acc-row" style="top:395px">
    <svg width="42" height="42" viewBox="0 0 42 42" fill="none" stroke="#333" stroke-width="1.6"><circle cx="26" cy="14" r="10"/><path d="M26 8v12M23 11h5a2 2 0 010 4h-4a2 2 0 000 4h5"/><path d="M4 40V28l8-4 8 6-6 3"/></svg>
    <span class="acc-label">Flexible Pricing</span><span class="acc-plus">+</span>
  </div>
  <div class="acc-rule" style="top:464px"></div>
  <div class="acc-row" style="top:478px">
    <svg width="42" height="42" viewBox="0 0 42 42" fill="none" stroke="#333" stroke-width="1.6"><path d="M14 28 L30 6 L36 6 L36 12 L14 28 Z"/><path d="M14 28l-6-2 6-8 6 0M14 28l2 6 8-6 0-6"/><path d="M8 36l4-4M5 31l3-2"/></svg>
    <span class="acc-label">Launch Campaign</span><span class="acc-plus">+</span>
  </div>
</section>

<section class="section" style="top:1624px;height:692px;background:var(--soft-bg)">
  <h2 class="abs center heading" style="top:46px"><span class="accent">Brevora</span> The Best</h2>
  <p class="abs center body-copy" style="top:108px">The All in One Platform to Generate Personalized Suggestions and<br>Hire Your Dream Team to Launch Winning Campaigns.</p>

  <div class="card-media" role="img" aria-label="Businessman holding a tablet with glowing growth charts" style="left:111px;top:235px;width:315px;height:186px;background:linear-gradient(135deg,#0c2340,#1d4f7d 55%,#0a1a30)"></div>
  <div class="card-title" style="left:111px;top:446px">No More Broken Promises</div>
  <p class="card-text" style="left:101px;top:482px">We guarantee quality marketing<br>professionals that deliver on time<br>and communicate constantly.</p>

  <div class="card-media" role="img" aria-label="Hand pointing at a rising 2024 bar chart above a laptop" style="left:443px;top:235px;width:314px;height:246px;background:linear-gradient(180deg,#c9cdd2,#8f969e 60%,#5c6269)"></div>
  <div class="card-title" style="left:443px;top:498px">Start at Nearly Any Budget</div>
  <p class="card-text" style="left:432px;top:531px">Simple, dynamic pricing within the<br>budget you select. Only pay for what you<br>use.</p>

  <div class="card-media" role="img" aria-label="Laptop with floating dashboard and analytics panels" style="left:774px;top:235px;width:314px;height:186px;background:linear-gradient(135deg,#9fc3df,#d7e5f1 50%,#7ea6c8)"></div>
  <div class="card-title" style="left:774px;top:446px">Transparency &amp; Control</div>
  <p class="card-text" style="left:764px;top:482px">View campaign progress and<br>update preferences at any time<br>through our convenient<br>application.</p>
</section>

<section class="section" style="top:2316px;height:544px">
  <h2 class="abs heading" style="left:110px;top:80px"><span class="accent">What People</span> Are Saying</h2>
  <p class="abs body-copy" style="left:110px;top:139px">Just a Few Out of Thousands of Happy Customers.</p>
  <p class="abs body-copy" style="left:110px;top:203px">Brevora did an excellent job recreating our website and is<br>doing an excellent job servicing our account as well. I would<br>highly recommend Brevora for any business.</p>
  <div class="abs" style="left:110px;top:326px;font-family:Montserrat,sans-serif;font-weight:500;font-size:22px;color:var(--blue)">MARCUS T</div>
  <div class="abs" style="left:110px;top:371px;font-family:Montserrat,sans-serif;font-weight:500;font-size:20px">OWNER</div>

  <span class="arrow" style="left:981px;top:113px;background:#000"><svg width="12" height="12" viewBox="0 0 12 12"><path d="M8 1 3 6l5 5" fill="none" stroke="#fff" stroke-width="2"/></svg></span>
  <span class="arrow" style="left:1054px;top:113px;background:var(--blue)"><svg width="12" height="12" viewBox="0 0 12 12"><path d="M4 1l5 5-5 5" fill="none" stroke="#fff" stroke-width="2"/></svg></span>

  <div class="avatar" role="img" aria-label="Portrait of customer Marcus T" style="left:684px;top:145px;width:304px;height:304px;background:linear-gradient(160deg,#d0d0d0,#8a8a8a)"></div>
  <div class="avatar" role="img" aria-label="Portrait of a smiling customer" style="left:1052px;top:201px;width:86px;height:86px;background:linear-gradient(160deg,#c9a68a,#6d6a66)"></div>
  <div class="avatar" role="img" aria-label="Portrait of a customer" style="left:980px;top:408px;width:66px;height:66px;background:linear-gradient(160deg,#8ba0a8,#6b4f42)"></div>
  <div class="avatar" role="img" aria-label="Portrait of a business owner" style="left:1115px;top:361px;width:98px;height:98px;background:linear-gradient(160deg,#e6e2dd,#9c7a62)"></div>
</section>

<section class="section" style="top:2860px;height:467px;background:var(--soft-bg)">
  <h2 class="abs heading" style="left:144px;top:47px"><span class="accent">Watch Brevora AI<br>Build an SEO<br>Optimized</span> Website<br>in Minutes.</h2>
  <p class="abs body-copy" style="left:145px;top:257px">Sign Up and Receive an Professional<br>Designed Website Same Day*</p>
  <a class="btn btn-solid" style="left:146px;top:353px;width:169px;height:49px">View Pricing</a>
  <a class="btn btn-ghost" style="left:328px;top:353px;width:167px;height:49px;font-size:16px">How It Works</a>

  <div class="stat" style="left:572px;top:48px">
    <svg width="56" height="54" viewBox="0 0 56 54" fill="none" stroke-width="2"><rect x="4" y="3" width="44" height="36" rx="3" stroke="#333"/><path d="M4 12h44" stroke="#333"/><path d="M17 22l-5 4 5 4M27 22l5 4-5 4" stroke="#333"/><circle cx="42" cy="40" r="7" stroke="#0094D4"/><circle cx="42" cy="40" r="2.5" stroke="#0094D4"/></svg>
    <div class="stat-num">4K+</div><div class="stat-label">Websites Built</div>
  </div>
  <div class="stat" style="left:832px;top:48px">
    <svg width="56" height="54" viewBox="0 0 56 54" fill="none" stroke-width="2"><circle cx="24" cy="16" r="9" stroke="#333"/><path d="M13 17a11 11 0 0122 0" stroke="#333"/><path d="M8 46c0-10 7-16 16-16s16 6 16 16" stroke="#333"/><circle cx="44" cy="34" r="8" stroke="#0094D4"/></svg>
    <div class="stat-num">2K</div><div class="stat-label">Consulting Hours</div>
  </div>
  <div class="stat" style="left:572px;top:240px">
    <svg width="56" height="54" viewBox="0 0 56 54" fill="none" stroke-width="2"><circle cx="32" cy="30" r="17" stroke="#333"/><path d="M32 30V20M32 30l7 5" stroke="#333"/><path d="M28 6h8M32 6v7" stroke="#333"/><path d="M4 24h8M2 31h9M5 38h7" stroke="#0094D4"/></svg>
    <div class="stat-num">&lt;1 HR</div><div class="stat-label">Avg Response Time</div>
  </div>
  <div class="stat" style="left:832px;top:240px">
    <svg width="56" height="54" viewBox="0 0 56 54" fill="none" stroke-width="2"><path d="M12 20V4M6 10l6-6 6 6" stroke="#333"/><circle cx="40" cy="14" r="11" stroke="#0094D4"/><path d="M35 19l10-10M36 10h1M43 18h1" stroke="#0094D4"/><rect x="4" y="28" width="16" height="6" stroke="#0094D4"/><rect x="4" y="36" width="16" height="6" stroke="#0094D4"/><rect x="4" y="44" width="40" height="6" stroke="#333"/></svg>
    <div class="stat-num">99%</div><div class="stat-label">Satisfaction Rate</div>
  </div>
</section>

<section class="section" style="top:3327px;height:402px">
  <h2 class="abs center heading" style="top:78px"><span class="accent">Companies We</span> Work With</h2>
  <div class="partner" style="left:111px;width:190px">Rankwell</div>
  <div class="partner" style="left:310px;width:188px;font-size:19px">Searchly Partner</div>
  <div class="partner" style="left:506px;width:189px">Tickerline</div>
  <div class="partner" style="left:703px;width:188px;font-size:18px">Funnelhub Academy</div>
  <div class="partner" style="left:900px;width:188px">Peakdesk</div>
  <span class="dot" style="left:546px"></span>
  <span class="dot" style="left:587px"></span>
  <span class="dot" style="left:628px"></span>
</section>

<footer class="section footer" style="top:3729px;height:492px">
  <div class="abs" style="left:172px;top:53px;font-family:Montserrat,sans-serif;font-weight:500;font-size:21px;color:var(--blue);letter-spacing:.4px">LET'S MAKE SOMETHING GREAT TOGETHER</div>
  <p class="abs" style="left:173px;top:101px;font-size:15px;font-weight:600">Start With Your Free Digital Marketing Roadmap.</p>
  <a class="btn btn-solid" style="left:772px;top:67px;width:256px;height:48px">Join the Revolution</a>
  <div class="abs" style="left:0;top:169px;width:1200px;height:1px;background:#2a2a2a"></div>

  <div class="brand" style="left:513px;top:198px;color:#fff"><span class="brand-mark"></span>brevora</div>

  <nav class="footer-links">
    <span>Marketing</span><span>|</span><span>Web Creation</span><span>|</span><span>Automation</span><span>|</span><span>Support</span>
  </nav>

  <span class="contact-dot" style="left:173px;top:337px"><svg width="16" height="22" viewBox="0 0 16 22"><path d="M8 1a7 7 0 017 7c0 5-7 13-7 13S1 13 1 8a7 7 0 017-7z" fill="#fff"/><circle cx="8" cy="8" r="2.6" fill="#0094D4"/></svg></span>
  <span class="contact-text" style="left:241px;top:349px">418 Linden Park Ave #12 Calder, GA 30991</span>
  <span class="contact-dot" style="left:678px;top:337px"><svg width="22" height="16" viewBox="0 0 22 16"><rect x="1" y="1" width="20" height="14" rx="1.5" fill="none" stroke="#fff" stroke-width="1.8"/><path d="M1 2l10 7 10-7" fill="none" stroke="#fff" stroke-width="1.8"/></svg></span>
  <span class="contact-text" style="left:747px;top:349px">hello@brevora.io</span>

  <div class="abs" style="left:0;top:418px;width:1200px;height:1px;background:#2a2a2a"></div>
  <span class="abs" style="left:113px;top:447px;font-family:Montserrat,sans-serif;font-weight:500;font-size:13px">COPYRIGHT © 2024 - BREVORA, INC.</span>
  <span class="social" style="left:981px;top:440px"></span>
  <span class="social" style="left:1018px;top:440px"></span>
  <span class="social" style="left:1056px;top:440px"></span>
</footer>

</body>
</html>
```